A DL (210mm wide x 100mm deep) layered .psd prepared for print ready CMYK 300 dpi for gloss paper.

Target Market(s)

Business People & young professionals – middle – high income earners.

Requirements
Must have
• Heading:
TOP Brunch (big and bold)
Traders Owners Partners (smaller underneath)

Text:
Everything about the TOP Brunch is TOP. The TOP Brunches are aimed at Traders, Owners and Partners and are designed to be an environment for where people Thrive, Offer and Prosper, while learning Trade, Openness and Prudence.

These events will be held on Friday mornings at 7am on February 17, May 18, August 17 and November 16, 2012.

The Velvet Playhouse, 412 Marlow Lane, Newcastle.
For more information, Phone (02) 4813 5062 or email info@chapel365.example

Please include:
SFP Logo, Chapel365 Logo, & TOP Logo
Nice to have
• Open to blue colours refer to steadyfundplanning.example and Chapel365.example

- Open to graphics/illustrations/photos - Can also purchase images from PixVault.
Should not have
• Too Much Bright Red or Yellow (open to some but not like a Burgertown flyer)

```html
<!DOCTYPE html>
<html lang="en">
<head>
<meta charset="utf-8">
<title>TOP Brunch – DL Flyer</title>
<link rel="stylesheet" href="https://fonts.googleapis.com/css2?family=PT+Serif:ital,wght@0,400;0,700;1,400&display=swap">
<style>
  :root {
    --navy-dark: #2d4766;
    --navy-mid: #5b7797;
    --navy-light: #8fa6c0;
    --sky: #1b9ad8;
    --ink: #44546f;
    --ink-dark: #2c3a52;
    --rule: #8a96a8;
    --paper: #ffffff;
    --paper-shade: #e6e9ee;
    --photo-a: #a9b9cc;
    --photo-b: #7f95ad;
    --photo-c: #c3ccd6;
  }
  * { margin: 0; padding: 0; box-sizing: border-box; }
  html, body { width: 1200px; height: 1200px; overflow: hidden; background: var(--paper); }
  .flyer {
    position: absolute; left: 37px; top: 343px;
    width: 1121px; height: 534px; overflow: hidden;
  }
  .flyer-backdrop { position: absolute; inset: 0; }
  .brand-panel {
    position: absolute; left: 0; top: 0; width: 420px; height: 534px;
    color: var(--paper); text-align: center; font-family: "PT Serif", serif;
  }
  .brand-heading {
    position: absolute; left: 0; right: 0; top: 190px;
    font-weight: 700; font-size: 66px; line-height: 1;
  }
  .brand-tagline {
    position: absolute; left: 0; right: 0; top: 276px;
    font-size: 22px; line-height: 1;
  }
  .photo-strip { position: absolute; top: 0; height: 151px; }
  .info-panel {
    position: absolute; left: 448px; width: 634px; top: 160px;
    text-align: center; font-family: "PT Serif", serif; color: var(--ink);
  }
  .info-heading { color: var(--sky); font-weight: 700; font-size: 21px; line-height: 28px; }
  .info-body { font-style: italic; font-size: 16.5px; line-height: 23px; margin-top: 2px; }
  .divider { display: block; margin: 8px auto; }
  .info-dates {
    font-variant: small-caps; font-size: 18.5px; line-height: 23px; color: var(--ink-dark);
    margin: 12px 0 10px;
  }
  .info-venue { font-style: italic; font-size: 15.5px; line-height: 23px; margin-top: 10px; white-space: nowrap; }
  .info-venue strong { font-style: normal; font-weight: 700; color: var(--ink-dark); }
  .partner-row {
    display: flex; justify-content: center; align-items: center; gap: 60px; margin-top: 14px;
  }
  .partner-name { font-size: 20px; line-height: 1; color: var(--ink-dark); }
</style>
</head>
<body>
<main class="flyer">
  <svg class="flyer-backdrop" width="1121" height="534" viewBox="0 0 1121 534" aria-hidden="true">
    <defs>
      <radialGradient id="panelGlow" cx="0.5" cy="0.45" r="0.75">
        <stop offset="0" stop-color="var(--navy-light)"/>
        <stop offset="0.55" stop-color="var(--navy-mid)"/>
        <stop offset="1" stop-color="var(--navy-dark)"/>
      </radialGradient>
      <linearGradient id="paperShade" x1="0" y1="0" x2="0" y2="1">
        <stop offset="0.25" stop-color="var(--paper-shade)"/>
        <stop offset="0.7" stop-color="var(--paper)"/>
      </linearGradient>
      <linearGradient id="edgeStrip" x1="0" y1="0" x2="0" y2="1">
        <stop offset="0" stop-color="var(--navy-light)"/>
        <stop offset="1" stop-color="var(--navy-dark)"/>
      </linearGradient>
    </defs>
    <rect width="1121" height="534" fill="url(#paperShade)"/>
    <polygon points="0,0 430,0 400,534 0,534" fill="url(#panelGlow)"/>
    <polygon points="1090,0 1121,0 1121,534 1078,534" fill="url(#edgeStrip)"/>
  </svg>

  <svg class="photo-strip" style="left:452px" width="209" height="151" role="img" aria-label="Photo: two business people chatting over coffee">
    <rect width="209" height="151" fill="var(--photo-a)"/>
  </svg>
  <svg class="photo-strip" style="left:664px" width="204" height="151" role="img" aria-label="Photo: office team celebrating with raised arms">
    <rect width="204" height="151" fill="var(--photo-b)"/>
  </svg>
  <svg class="photo-strip" style="left:871px" width="208" height="151" role="img" aria-label="Photo: colleagues joining hands in a high five">
    <rect width="208" height="151" fill="var(--photo-c)"/>
  </svg>

  <section class="brand-panel">
    <h1 class="brand-heading">TOP Brunch</h1>
    <p class="brand-tagline">Traders Owners Partners</p>
  </section>

  <section class="info-panel">
    <h2 class="info-heading">Bringing Traders, Owners and Partners together</h2>
    <p class="info-body">Everything about the TOP Brunch is TOP. The TOP Brunches are aimed at Traders, Owners and Partners and are designed to be an environment for where people Thrive, Offer and Prosper, while learning Trade, Openness and Prudence.</p>
    <svg class="divider" width="540" height="10" aria-hidden="true">
      <line x1="0" y1="5" x2="540" y2="5" stroke="var(--rule)" stroke-width="1" stroke-dasharray="4 3"/>
      <circle cx="270" cy="5" r="4" fill="var(--paper)" stroke="var(--rule)"/>
      <circle cx="270" cy="5" r="1.8" fill="var(--ink)"/>
    </svg>
    <p class="info-dates">These events will be held on Friday mornings at 7am<br>on February 17, May 18, August 17 and November 16, 2012.</p>
    <svg class="divider" width="540" height="10" aria-hidden="true">
      <line x1="0" y1="5" x2="540" y2="5" stroke="var(--rule)" stroke-width="1" stroke-dasharray="4 3"/>
      <circle cx="270" cy="5" r="4" fill="var(--paper)" stroke="var(--rule)"/>
      <circle cx="270" cy="5" r="1.8" fill="var(--ink)"/>
    </svg>
    <p class="info-venue">The Velvet Playhouse, 412 Marlow Lane, Newcastle.<br>For more information, Phone <strong>(02) 4813 5062</strong> or email <strong>info@chapel365.example</strong></p>
    <div class="partner-row">
      <span class="partner-name">SFP</span>
      <span class="partner-name">Chapel365</span>
    </div>
  </section>
</main>
</body>
</html>
```